Medical Herbalist needs labels for healing skin salves

I am bringing out a Calendula Salve and a Comfrey and Meadowsweet Salve, both have healing qualities and have have a history of Traditional use. I would like the label to look eye-cathching and colourful, orange based for Calendula and Green based for Comfrey. I particularly like Varembelle's image and their font. (skin care range - please look at this) I want to convey a sense of the Apothecary (most important) and slightly retro, old fashioned, quality about these salves.
I would like a design to fit on a label that goes around a 30ml or 60ml jar - I will be using both. I feel that the usp is that I am a Medical Herbalist producing hand made, containing natural ingredients - quality items made in Wales. (part of the UK) I have considered calling them Tidy Tins but not definite about this yet.
Measurements:
60ml jar - 31mm (height) x 150 to 160mm width - i.e. around the jar
30ml jar 18mm (height) x 105mm to 125mm width - i.e. around the jar

Reason: I would like to see some more designs before I make my decisions - I have not had enough that I am excited about so far I am afraid.

Target Market(s)

Adults, male and female but female bias. Wanting to solve problem i.e. dry chapped skin, cracked heals (Calendula). Sprains, aches and pains (Comfrey and Meadowsweet)

Industry/Entity Type

Medical

Font styles to use
Serif
Decorative

Colors
acd036
cadf82
e9f1ce
f79020
fece3e
faa54b

Requirements
Must have
• The kind of font and look I have suggested. Clearly Calendula Salve in large writing
and the same for the Comfrey and Meadowsweet Salve. It needs to have some impact
I need to have room to list ingredients.
Nice to have
• Possible images of the plants or part of the plants listed. I was not intending the photographs to be used - they were more to inspire hopefully.
Picture of pestle and mortar?
Should not have
• Anything too jokey or gimmicky.

```html
<!DOCTYPE html>
<html lang="en">
<head>
<meta charset="utf-8">
<title>Tidy Tins – Salve Labels</title>
<link rel="stylesheet" href="https://fonts.googleapis.com/css2?family=Cormorant+SC:wght@500;600&family=Playfair+Display:ital@1&family=Libre+Baskerville&display=swap">
<style>
  :root {
    --orange: #f7931e;
    --orange-soft: #fbc98c;
    --green: #a9cf38;
    --green-soft: #d3e6a4;
    --tan: #cdb98f;
    --tan-dark: #bfa97c;
    --cream: #fbf5e3;
    --cream-line: #eee4c8;
    --ink: #4a3b2c;
    --white: #ffffff;
  }
  html, body {
    margin: 0;
    padding: 0;
    width: 1200px;
    height: 1200px;
    overflow: hidden;
    background: var(--white);
  }
  .sheet { display: block; width: 1200px; height: 1200px; }

  .label--calendula { --accent: var(--orange); --accent-soft: var(--orange-soft); }
  .label--comfrey { --accent: var(--green); --accent-soft: var(--green-soft); }

  .wrap-band__fill { fill: var(--accent); }
  .wrap-band__stripe { stroke: var(--white); stroke-width: 1.6; }
  .seal__ring { fill: var(--tan); }
  .seal__face { fill: var(--cream); }
  .seal__rule { fill: none; stroke: var(--tan); stroke-width: 0.8; }
  .seal__art { fill: var(--accent-soft); opacity: 0.55; }
  .seal__caption { font-family: "Cormorant SC", serif; font-size: 8px; letter-spacing: 1.5px; fill: var(--tan-dark); }

  .label__outline { fill: var(--tan); }
  .label__ground { fill: var(--cream); }
  .label__panel { fill: url(#pinstripe); }
  .label__frame { fill: none; stroke: var(--accent); stroke-width: 11; }
  .label__dots { fill: none; stroke: var(--white); stroke-width: 2.2; stroke-dasharray: 0.1 5; stroke-linecap: round; }
  .label__art { fill: var(--accent-soft); opacity: 0.5; }
  .label__arc-text { font-family: "Libre Baskerville", serif; font-size: 11.5px; letter-spacing: 3px; fill: var(--ink); }
  .star { fill: var(--tan-dark); }

  .ribbon { fill: var(--tan); }
  .ribbon__edge { fill: var(--tan-dark); opacity: 0.35; }
  .cartouche__ring { fill: var(--tan); }
  .cartouche__face { fill: var(--cream); }
  .cartouche__rule { fill: none; stroke: var(--tan); stroke-width: 1; }
  .cartouche__line { stroke: var(--ink); stroke-width: 0.6; opacity: 0.6; }
  .brand-dot { fill: var(--tan-dark); }
  .brand-name { font-family: "Cormorant SC", serif; font-weight: 500; font-size: 15px; letter-spacing: 0.6px; fill: var(--ink); }
  .product-name { font-family: "Playfair Display", serif; font-style: italic; fill: var(--ink); }
  .product-use { font-family: "Cormorant SC", serif; font-weight: 600; font-size: 7.5px; fill: var(--ink); }
  .footer-line { font-family: "Libre Baskerville", serif; font-size: 14.5px; letter-spacing: 0.4px; fill: var(--ink); }
</style>
</head>
<body>
<svg class="sheet" viewBox="0 0 1200 1200" xmlns="http://www.w3.org/2000/svg">
  <defs>
    <pattern id="pinstripe" width="12" height="12" patternUnits="userSpaceOnUse">
      <rect width="12" height="12" fill="#fbf5e3"/>
      <line x1="6" y1="0" x2="6" y2="12" stroke="#efe6cb" stroke-width="1"/>
    </pattern>
    <path id="arc-main" d="M334,352 A74,74 0 0 1 474,352"/>
    <path id="arc-seal" d="M369,148 A36,36 0 0 1 439,148"/>
    <g id="stars">
      <polygon class="star" points="0,-4 1.2,-1.2 4,-1.2 1.8,0.6 2.6,3.6 0,1.8 -2.6,3.6 -1.8,0.6 -4,-1.2 -1.2,-1.2"/>
    </g>
  </defs>

  <!-- Calendula -->
  <g class="label label--calendula">
    <g class="wrap-band">
      <rect class="wrap-band__fill" x="263" y="110" width="283" height="96"/>
      <g>
        <line class="wrap-band__stripe" x1="263" y1="122" x2="546" y2="122"/>
        <line class="wrap-band__stripe" x1="263" y1="134" x2="546" y2="134"/>
        <line class="wrap-band__stripe" x1="263" y1="146" x2="546" y2="146"/>
        <line class="wrap-band__stripe" x1="263" y1="158" x2="546" y2="158"/>
        <line class="wrap-band__stripe" x1="263" y1="170" x2="546" y2="170"/>
        <line class="wrap-band__stripe" x1="263" y1="182" x2="546" y2="182"/>
        <line class="wrap-band__stripe" x1="263" y1="194" x2="546" y2="194"/>
      </g>
      <circle class="seal__ring" cx="404" cy="158" r="64"/>
      <circle class="seal__face" cx="404" cy="158" r="55"/>
      <circle class="seal__rule" cx="404" cy="158" r="50"/>
      <text class="seal__caption"><textPath href="#arc-seal" startOffset="50%" text-anchor="middle">PREMIUM QUALITY</textPath></text>
      <ellipse class="seal__art" cx="404" cy="160" rx="18" ry="24" role="img" aria-label="Small calendula flower sketch"/>
      <use href="#stars" x="394" y="198" transform="scale(1)"/>
      <use href="#stars" x="404" y="200"/>
      <use href="#stars" x="414" y="198"/>
    </g>

    <g class="main-label">
      <path class="label__outline" d="M263,338 H290 V332 C290,292 340,266 404,266 C468,266 518,292 518,332 V338 H546 V992 H263 Z"/>
      <path class="label__ground" d="M267,342 H294 V332 C294,296 342,270 404,270 C466,270 514,296 514,332 V342 H542 V988 H267 Z"/>
      <path class="label__panel" d="M281,357 H308 V336 C308,304 353,285 404,285 C455,285 500,304 500,336 V357 H528 V974 H281 Z"/>
      <path class="label__frame" d="M281,357 H308 V336 C308,304 353,285 404,285 C455,285 500,304 500,336 V357 H528 V974 H281 Z"/>
      <path class="label__dots" d="M281,357 H308 V336 C308,304 353,285 404,285 C455,285 500,304 500,336 V357 H528 V974 H281 Z"/>
      <text class="label__arc-text"><textPath href="#arc-main" startOffset="50%" text-anchor="middle">PREMIUM QUALITY</textPath></text>
      <use href="#stars" x="380" y="344"/>
      <use href="#stars" x="404" y="336"/>
      <use href="#stars" x="428" y="344"/>
      <rect class="label__art" x="305" y="378" width="198" height="326" rx="40" role="img" aria-label="Botanical line drawing of a calendula plant in orange"/>

      <rect class="ribbon" x="263" y="779" width="283" height="82"/>
      <rect class="ribbon__edge" x="263" y="779" width="18" height="82"/>
      <rect class="ribbon__edge" x="528" y="779" width="18" height="82"/>
      <ellipse class="cartouche__ring" cx="404" cy="817" rx="97" ry="84"/>
      <ellipse class="cartouche__face" cx="404" cy="817" rx="89" ry="76"/>
      <ellipse class="cartouche__rule" cx="404" cy="817" rx="83" ry="70"/>
      <circle class="brand-dot" cx="404" cy="757" r="12"/>
      <text class="brand-name" x="404" y="791" text-anchor="middle">Tidy Tins</text>
      <line class="cartouche__line" x1="340" y1="799" x2="468" y2="799"/>
      <text class="product-name" x="406" y="824" text-anchor="middle" font-size="19">Calendula Salve</text>
      <line class="cartouche__line" x1="340" y1="838" x2="468" y2="838"/>
      <text class="product-use" x="404" y="856" text-anchor="middle">Dry Chapped Skin, Cracked Heals</text>

      <text class="footer-line" x="406" y="944" text-anchor="middle">HAND MADE SKINCARE</text>
    </g>
  </g>

  <!-- Comfrey & Meadowsweet -->
  <g class="label label--comfrey" transform="translate(362 0)">
    <g class="wrap-band">
      <rect class="wrap-band__fill" x="263" y="110" width="283" height="96"/>
      <g>
        <line class="wrap-band__stripe" x1="263" y1="122" x2="546" y2="122"/>
        <line class="wrap-band__stripe" x1="263" y1="134" x2="546" y2="134"/>
        <line class="wrap-band__stripe" x1="263" y1="146" x2="546" y2="146"/>
        <line class="wrap-band__stripe" x1="263" y1="158" x2="546" y2="158"/>
        <line class="wrap-band__stripe" x1="263" y1="170" x2="546" y2="170"/>
        <line class="wrap-band__stripe" x1="263" y1="182" x2="546" y2="182"/>
        <line class="wrap-band__stripe" x1="263" y1="194" x2="546" y2="194"/>
      </g>
      <circle class="seal__ring" cx="404" cy="158" r="64"/>
      <circle class="seal__face" cx="404" cy="158" r="55"/>
      <circle class="seal__rule" cx="404" cy="158" r="50"/>
      <text class="seal__caption"><textPath href="#arc-seal" startOffset="50%" text-anchor="middle">PREMIUM QUALITY</textPath></text>
      <ellipse class="seal__art" cx="404" cy="160" rx="18" ry="24" role="img" aria-label="Small comfrey flower sketch"/>
      <use href="#stars" x="394" y="198"/>
      <use href="#stars" x="404" y="200"/>
      <use href="#stars" x="414" y="198"/>
    </g>

    <g class="main-label">
      <path class="label__outline" d="M263,338 H290 V332 C290,292 340,266 404,266 C468,266 518,292 518,332 V338 H546 V992 H263 Z"/>
      <path class="label__ground" d="M267,342 H294 V332 C294,296 342,270 404,270 C466,270 514,296 514,332 V342 H542 V988 H267 Z"/>
      <path class="label__panel" d="M281,357 H308 V336 C308,304 353,285 404,285 C455,285 500,304 500,336 V357 H528 V974 H281 Z"/>
      <path class="label__frame" d="M281,357 H308 V336 C308,304 353,285 404,285 C455,285 500,304 500,336 V357 H528 V974 H281 Z"/>
      <path class="label__dots" d="M281,357 H308 V336 C308,304 353,285 404,285 C455,285 500,304 500,336 V357 H528 V974 H281 Z"/>
      <text class="label__arc-text"><textPath href="#arc-main" startOffset="50%" text-anchor="middle">PREMIUM QUALITY</textPath></text>
      <use href="#stars" x="380" y="344"/>
      <use href="#stars" x="404" y="336"/>
      <use href="#stars" x="428" y="344"/>
      <rect class="label__art" x="298" y="376" width="214" height="334" rx="40" role="img" aria-label="Botanical line drawing of a flowering comfrey and meadowsweet stem in green"/>

      <rect class="ribbon" x="263" y="779" width="283" height="82"/>
      <rect class="ribbon__edge" x="263" y="779" width="18" height="82"/>
      <rect class="ribbon__edge" x="528" y="779" width="18" height="82"/>
      <ellipse class="cartouche__ring" cx="404" cy="817" rx="97" ry="84"/>
      <ellipse class="cartouche__face" cx="404" cy="817" rx="89" ry="76"/>
      <ellipse class="cartouche__rule" cx="404" cy="817" rx="83" ry="70"/>
      <circle class="brand-dot" cx="404" cy="757" r="12"/>
      <text class="brand-name" x="404" y="791" text-anchor="middle">Tidy Tins</text>
      <line class="cartouche__line" x1="340" y1="797" x2="468" y2="797"/>
      <text class="product-name" x="404" y="812" text-anchor="middle" font-size="15.5">Comfrey &amp;</text>
      <text class="product-name" x="404" y="831" text-anchor="middle" font-size="15.5">Meadowsweet Salve</text>
      <line class="cartouche__line" x1="340" y1="840" x2="468" y2="840"/>
      <text class="product-use" x="404" y="856" text-anchor="middle">Sprains, Aches and Pains</text>

      <text class="footer-line" x="406" y="944" text-anchor="middle">HAND MADE SKINCARE</text>
    </g>
  </g>
</svg>
</body>
</html>
```